Social Movement/Church Plant Website - KindAshbury.com

We need a website for our church plant startup, however we want the focus of the landing page to be around #kindashbury - that we are an organization that is FOR our town (Ashbury). The site will include serving project events, social events, a place to sign up for emails, a blog, a place to give, etc. All the elements we know we want are currently at kindashbury.com . Please check this for copy.

We want this to be easy to edit as a non-developer.

I have included several logos with our colors, as well as an ai file to give you an idea of how we want the design to look and feel - also includes our branded fonts

Target Market(s)

People who live in the Northern CO area

Font styles to use
Serif
Sans Serif

Requirements
Must have
• Events (serve and social), Blog section, A place to get involved - where to give and to sign up for emails. Must match our branding colors and style hex 4c7991.
Should not have
• Should not be focused on the actual church plant on the home page. There can be some back end stuff about it, but the focus should be #kindashbury.

```html
<!DOCTYPE html>
<html lang="en">
<head>
<meta charset="utf-8">
<title>Harbor Light Church – #KINDASHBURY</title>
<link rel="stylesheet" href="https://fonts.googleapis.com/css2?family=Cinzel:wght@400;600&family=Quicksand:wght@500;700&family=Lato:ital,wght@0,400;0,700;1,400&display=swap">
<style>
:root{
  --blue:#1f8fd3;
  --blue-dark:#1c6fa3;
  --brand:#4c7991;
  --button:#2f6684;
  --ink:#333b42;
  --muted:#8a9197;
  --white:#ffffff;
  --star:#f6c21b;
  --footer-a:#2596d6;
  --footer-b:#17679a;
}
*{box-sizing:border-box;margin:0;padding:0}
html,body{width:1200px;height:3830px;overflow:hidden}
body{font-family:'Lato',sans-serif;color:var(--ink);background:var(--white);position:relative}
.heading{font-family:'Quicksand',sans-serif;font-weight:700}

/* Hero */
.hero{position:absolute;left:0;top:0;width:1200px;height:677px;overflow:hidden}
.hero-photo{position:absolute;inset:0;background:
  radial-gradient(ellipse at 75% 30%,rgba(120,150,80,.55),transparent 55%),
  linear-gradient(120deg,#4f6b3c 0%,#7c8f55 30%,#3e5a33 55%,#2f4b5e 80%,#4a6d8a 100%)}
.hero-shade{position:absolute;inset:0;background:rgba(10,20,15,.35)}
.brand-name{position:absolute;left:0;width:1200px;top:150px;text-align:center;font-family:'Cinzel',serif;font-weight:600;font-size:38px;letter-spacing:4px;color:var(--white)}
.main-nav{position:absolute;left:0;width:1200px;top:307px;display:flex;justify-content:center;gap:44px}
.main-nav a{color:var(--white);text-decoration:none;font-weight:700;font-size:17px;letter-spacing:.5px}
.hero-rule{position:absolute;left:350px;width:500px;height:1px;background:rgba(255,255,255,.8)}
.hero-title{position:absolute;left:0;width:1200px;top:370px;text-align:center;font-family:'Cinzel',serif;font-weight:400;font-size:64px;letter-spacing:10px;color:var(--white)}
.hero-btn{position:absolute;left:505px;top:497px;width:190px;height:60px;border-radius:30px;background:var(--white);color:var(--brand);font-weight:700;font-size:18px;display:flex;align-items:center;justify-content:center;letter-spacing:.5px}

/* Welcome */
.welcome-title{position:absolute;left:0;width:1200px;top:734px;text-align:center;font-size:36px;color:var(--blue)}
.welcome-line{position:absolute;top:759px;width:100px;height:1px;background:#c8d3da}
.welcome-sub{position:absolute;left:0;width:1200px;top:812px;text-align:center;font-size:21px;font-family:'Quicksand',sans-serif;font-weight:500;color:var(--ink)}
.welcome-text{position:absolute;left:220px;width:760px;top:860px;text-align:center;font-size:14.5px;line-height:24px;color:var(--muted)}
.action{position:absolute;top:996px;width:200px;text-align:center}
.action-icon{width:118px;height:118px;margin:0 auto;border-radius:50%;border:6px solid var(--blue-dark);background:var(--white);box-shadow:0 4px 10px rgba(0,0,0,.15);display:flex;align-items:center;justify-content:center}
.action-label{margin-top:28px;font-family:'Quicksand',sans-serif;font-weight:700;font-size:19px;color:var(--blue-dark);letter-spacing:.5px}
.contact-pill{position:absolute;left:460px;top:1212px;width:280px;height:60px;border-radius:30px;background:var(--blue);color:var(--white);display:flex;align-items:center;justify-content:center;gap:12px;font-size:17px}

/* Events */
.events{position:absolute;left:0;top:1348px;width:1200px;height:630px;background:linear-gradient(135deg,#1f8ccd 0%,#1f86c6 50%,#2470a0 100%)}
.section-title-light{position:absolute;left:0;width:1200px;top:54px;text-align:center;font-size:37px;color:var(--white)}
.event-card{position:absolute;top:138px;width:248px;height:416px;background:var(--white);padding:12px;text-align:center}
.event-photo{width:224px;height:156px}
.event-name{margin-top:30px;font-family:'Quicksand',sans-serif;font-weight:700;font-size:18px;line-height:26px;color:var(--blue);height:52px;display:flex;align-items:center;justify-content:center}
.event-meta{margin-top:8px;font-size:13.5px;line-height:23px;color:var(--ink)}
.event-btn{position:absolute;left:40px;bottom:42px;width:168px;height:48px;border-radius:24px;background:var(--button);color:var(--white);font-size:14.5px;font-weight:700;display:flex;align-items:center;justify-content:center;letter-spacing:.5px}

/* Photo feed */
.section-title-blue{position:absolute;left:0;width:1200px;text-align:center;font-size:37px;color:var(--blue)}
.feed-tile{position:absolute;top:2129px;width:240px;height:238px;overflow:hidden;display:flex;align-items:center;justify-content:center;color:var(--white)}

/* Contact & reviews */
.reviews-band{position:absolute;left:0;top:2502px;width:1200px;height:472px;background:linear-gradient(120deg,#26301f 0%,#3a4a30 35%,#2a3328 65%,#1c2420 100%)}
.reviews-shade{position:absolute;inset:0;background:rgba(0,0,0,.4)}
.contact-box{position:absolute;left:77px;top:2451px;width:467px;height:574px;background:var(--blue);padding:36px 33px}
.contact-box h2{font-size:36px;color:var(--white);margin-bottom:20px}
.field{background:var(--white);height:56px;margin-bottom:18px;padding:18px 16px;font-size:14px;color:#555}
.field.message{height:90px}
.submit-btn{margin:16px auto 0;width:186px;height:58px;border-radius:29px;background:var(--button);color:var(--white);font-size:18px;font-weight:700;display:flex;align-items:center;justify-content:center;letter-spacing:.5px}
.review-title{position:absolute;left:610px;top:2560px;font-size:34px;color:var(--white)}
.avatar{position:absolute;left:608px;top:2630px;width:100px;height:100px;border-radius:50%;border:4px solid var(--white);background:linear-gradient(160deg,#dfe7ee,#b9c8d4)}
.reviewer{position:absolute;left:735px;top:2668px;color:var(--white);font-size:15px;font-weight:700;letter-spacing:.5px}
.reviewer-role{position:absolute;left:735px;top:2694px;color:#d8dde1;font-size:12px}
.stars{position:absolute;left:735px;top:2710px;color:var(--star);font-size:15px;letter-spacing:2px}
.review-text{position:absolute;left:610px;top:2764px;width:520px;color:var(--white);font-size:17px;line-height:36px;font-style:italic}
.dots{position:absolute;left:608px;top:2882px;display:flex;gap:8px}
.dots span{width:12px;height:12px;border-radius:50%;border:2px solid var(--white)}
.dots span.on{background:var(--blue)}

/* News */
.news-title{position:absolute;left:79px;top:3152px;font-size:37px;line-height:44px;color:var(--blue)}
.news-text{position:absolute;left:79px;top:3258px;width:320px;font-size:13.5px;line-height:22px;color:#555}
.view-all{position:absolute;left:77px;top:3370px;width:136px;height:58px;border-radius:29px;background:var(--button);color:var(--white);font-size:17px;font-weight:700;display:flex;align-items:center;justify-content:center}
.news-card{position:absolute;top:3090px;width:318px;height:396px;background:var(--white);box-shadow:0 2px 10px rgba(0,0,0,.1);padding:6px}
.news-photo{width:306px;height:206px}
.news-card h3{margin-top:24px;text-align:center;font-family:'Quicksand',sans-serif;font-weight:700;font-size:18px;line-height:28px;color:var(--blue)}
.news-meta{position:absolute;left:16px;right:16px;bottom:22px;display:flex;align-items:center;font-size:12px;color:#777;border-top:1px solid #eee;padding-top:14px}
.news-meta .link{margin-left:40px;font-style:italic;color:#999}
.news-meta .heart{margin-left:auto}

/* Footer */
.site-footer{position:absolute;left:0;top:3566px;width:1200px;height:264px;background:linear-gradient(120deg,var(--footer-a) 0%,#1e7fbd 55%,var(--footer-b) 100%);color:var(--white)}
.footer-head{position:absolute;top:46px;font-family:'Quicksand',sans-serif;font-weight:700;font-size:26px}
.footer-phone{position:absolute;left:79px;top:96px;font-size:22px;font-weight:700}
.footer-mail{position:absolute;left:79px;top:130px;font-size:14px}
.newsletter{position:absolute;left:437px;top:95px;width:316px;height:62px;background:var(--white);color:#333;font-size:14px;display:flex;align-items:center;justify-content:space-between;padding:0 16px}
.social{position:absolute;left:863px;top:93px;display:flex;gap:10px}
.social span{width:38px;height:38px;border-radius:50%;border:2px solid var(--white);display:block}
.footer-rule{position:absolute;left:0;top:202px;width:1200px;height:1px;background:rgba(255,255,255,.35)}
.copyright{position:absolute;left:79px;top:224px;font-size:13px}
.legal{position:absolute;right:79px;top:224px;font-size:13px}
</style>
</head>
<body>

<header class="hero">
  <div class="hero-photo" role="img" aria-label="Volunteer carrying rolls of fresh sod on a green lawn"></div>
  <div class="hero-shade"></div>
  <div class="brand-name">HARBOR LIGHT CHURCH</div>
  <nav class="main-nav">
    <a href="#">HOME</a><a href="#">ABOUT</a><a href="#">EVENTS</a><a href="#">BLOG</a><a href="#">GIVE</a><a href="#">CONTACT US</a>
  </nav>
  <div class="hero-rule" style="top:364px"></div>
  <h1 class="hero-title">#KINDASHBURY</h1>
  <div class="hero-rule" style="top:450px"></div>
  <div class="hero-btn">LEARN MORE</div>
</header>

<section class="welcome">
  <div class="welcome-line" style="left:265px"></div>
  <h2 class="welcome-title heading">Welcome # KINDASHBURY</h2>
  <div class="welcome-line" style="left:835px"></div>
  <p class="welcome-sub">Working Toward a Better Tomorrow</p>
  <p class="welcome-text">We are for the broken and the brand new, the beautifully painted and the terribly stained. We are for the addict and the aristocrat, the put together and the never been messier. We are for families and individuals, for the unloved and the unwanted. We are for the workaholic and the in-between-jobber, the ones who grew up here and these who just got here. We are for a better tomorrow. We are for our city. We are For Ashbury.</p>

  <div class="action" style="left:230px">
    <div class="action-icon">
      <svg width="56" height="60" viewBox="0 0 56 60" fill="none" stroke="#3a4a55" stroke-width="3" stroke-linejoin="round"><path d="M14 34V12a4 4 0 0 1 8 0v16V6a4 4 0 0 1 8 0v22V9a4 4 0 0 1 8 0v21V16a4 4 0 0 1 8 0v22c0 12-8 19-18 19-8 0-13-4-17-11L5 34a4 4 0 0 1 7-4z"/></svg>
    </div>
    <div class="action-label">GET INVOLVED</div>
  </div>
  <div class="action" style="left:497px">
    <div class="action-icon">
      <svg width="70" height="50" viewBox="0 0 70 50" fill="none" stroke="#3a4a55" stroke-width="3" stroke-linejoin="round" stroke-linecap="round"><path d="M2 14l12-8 10 4h10"/><path d="M68 14l-12-8-14 6-10 8a4 4 0 0 0 6 5l8-5 16 14"/><path d="M14 6l-12 22 8 6"/><path d="M56 6l12 22-6 6"/><path d="M10 34l8 8a3 3 0 0 0 5-4M18 36l8 8a3 3 0 0 0 5-4M26 38l6 6a3 3 0 0 0 5-4M34 40l4 4a3 3 0 0 0 5-4l-2-2"/></svg>
    </div>
    <div class="action-label">PARTNERSHIP</div>
  </div>
  <div class="action" style="left:768px">
    <div class="action-icon">
      <svg width="60" height="60" viewBox="0 0 60 60"><rect x="12" y="4" width="36" height="14" rx="2" fill="#3a4a55"/><text x="30" y="14.5" font-family="Lato,sans-serif" font-size="8" font-weight="700" fill="#fff" text-anchor="middle">DONATE</text><path d="M8 30h44v26H8z" fill="none" stroke="#3a4a55" stroke-width="3"/><path d="M30 22v16M24 32l6 6 6-6" fill="none" stroke="#3a4a55" stroke-width="3" stroke-linecap="round" stroke-linejoin="round"/></svg>
    </div>
    <div class="action-label">DONATE</div>
  </div>

  <div class="contact-pill">
    <svg width="20" height="20" viewBox="0 0 24 24" fill="#fff"><path d="M6.6 10.8a15 15 0 0 0 6.6 6.6l2.2-2.2a1 1 0 0 1 1-.25 11.4 11.4 0 0 0 3.6.57 1 1 0 0 1 1 1V20a1 1 0 0 1-1 1A17 17 0 0 1 3 4a1 1 0 0 1 1-1h3.5a1 1 0 0 1 1 1c0 1.25.2 2.45.57 3.57a1 1 0 0 1-.25 1z"/></svg>
    <span>Contact - <strong>123-456-789</strong></span>
  </div>
</section>

<section class="events">
  <h2 class="section-title-light heading">Upcoming Events</h2>
  <article class="event-card" style="left:79px">
    <div class="event-photo" role="img" aria-label="Kids holding a recycling bin during a school cleanup" style="background:linear-gradient(160deg,#8fbf5a,#4f8a3a 60%,#2f7fb8)"></div>
    <h3 class="event-name">School Cleanup</h3>
    <p class="event-meta">Jul 28 5:00 PM – 6:00 PM<br>Location is TBD</p>
    <div class="event-btn">REGISTER NOW</div>
  </article>
  <article class="event-card" style="left:347px">
    <div class="event-photo" role="img" aria-label="Family picnic on a blanket with a dog" style="background:linear-gradient(160deg,#a9c77a,#6e9a4c 55%,#c9a98a)"></div>
    <h3 class="event-name">Corn Roast Festival</h3>
    <p class="event-meta">Aug 04, 5:00 PM – 10:00 PM<br>Location is TBD</p>
    <div class="event-btn">REGISTER NOW</div>
  </article>
  <article class="event-card" style="left:618px">
    <div class="event-photo" role="img" aria-label="Children running together in a park" style="background:linear-gradient(160deg,#7fae57,#5a8d3e 55%,#9bb56c)"></div>
    <h3 class="event-name">Building Gaga Pit for Local School</h3>
    <p class="event-meta">Jul 14, 9:00 AM – 12:00 PM<br>Ashbury Classical School</p>
    <div class="event-btn">REGISTER NOW</div>
  </article>
  <article class="event-card" style="left:886px">
    <div class="event-photo" role="img" aria-label="Friends relaxing in a swimming pool" style="background:linear-gradient(160deg,#9fd3df,#4fa7c0 55%,#c8b6a0)"></div>
    <h3 class="event-name">Pool Party</h3>
    <p class="event-meta">Jul 26, 5:30 PM – 7:30 PM<br>Maple Outdoor Pool, 2740…</p>
    <div class="event-btn">REGISTER NOW</div>
  </article>
</section>

<section class="photo-feed">
  <h2 class="section-title-blue heading" style="top:2034px">Follow Us On Picturely</h2>
  <div class="feed-tile" style="left:77px;background:linear-gradient(160deg,#8d98a8,#5f6b7c)" role="img" aria-label="Gloved hand with event hashtag">
    <span style="font-family:'Cinzel',serif;font-size:24px;letter-spacing:2px">#KINDASHBURY</span>
  </div>
  <div class="feed-tile" style="left:347px;background:linear-gradient(160deg,#6f7a5a,#4a5440)" role="img" aria-label="Volunteers working on a garden project">
    <span style="background:rgba(0,0,0,.45);position:absolute;inset:0"></span>
    <span style="position:relative;display:flex;align-items:center;gap:8px;font-size:20px">
      <svg width="22" height="20" viewBox="0 0 24 22" fill="none" stroke="#fff" stroke-width="2"><path d="M12 20S2 13.5 2 7a5 5 0 0 1 10-1 5 5 0 0 1 10 1c0 6.5-10 13-10 13z"/></svg>11
      <svg width="22" height="20" viewBox="0 0 24 22" fill="none" stroke="#fff" stroke-width="2" style="margin-left:16px"><path d="M3 10a9 8 0 1 1 4 6.6L3 19z"/></svg>0
    </span>
  </div>
  <div class="feed-tile" style="left:615px;background:linear-gradient(160deg,#5b5b5b,#2b2b2b)" role="img" aria-label="Black and white quote graphic">
    <span style="width:180px;text-align:center;font-family:'Cinzel',serif;font-size:13px;line-height:19px;background:rgba(0,0,0,.55);padding:6px">Because of what Jesus has done, death, sickness, and woundedness never have to hold us prisoner again</span>
  </div>
  <div class="feed-tile" style="left:883px;background:linear-gradient(180deg,#3a8ad6 0%,#6fb0e6 45%,#6e9a48 62%,#4d7f33 100%)" role="img" aria-label="Bounce house on a lawn at a community event"></div>
</section>

<section class="reviews">
  <div class="reviews-band" role="img" aria-label="Dark leafy foliage background"><div class="reviews-shade"></div></div>
  <form class="contact-box">
    <h2 class="heading">Contact Us</h2>
    <div class="field">Name :</div>
    <div class="field">Phone :</div>
    <div class="field">Email :</div>
    <div class="field message">Message :</div>
    <div class="submit-btn">SUBMIT NOW</div>
  </form>
  <h2 class="review-title heading">Clients Reviews</h2>
  <div class="avatar" role="img" aria-label="Reviewer portrait"></div>
  <div class="reviewer">MAYA RENFIELD</div>
  <div class="reviewer-role">Genuine Customer</div>
  <div class="stars">★★★★<span style="color:#8a8f93">★</span></div>
  <p class="review-text">Lorem Ipsum is simply dummy text of the printing and typesetting industry. Lorem Ipsum has been the industry's</p>
  <div class="dots"><span class="on"></span><span></span><span></span><span></span></div>
</section>

<section class="news">
  <h2 class="news-title heading">Latest News &amp;<br>Updates</h2>
  <p class="news-text">Fruit is their fill meat hath abundantly place meat don't stars so and which signs third second after seasons under.</p>
  <div class="view-all">VIEW ALL</div>
  <article class="news-card" style="left:442px">
    <div class="news-photo" role="img" aria-label="Volunteers planting in a community garden" style="background:linear-gradient(160deg,#9cc46a,#5f8f3d 55%,#7a5a3a)"></div>
    <h3>What Is It Like To Help With a<br>Build-a-Home Project?</h3>
    <div class="news-meta">
      <svg width="20" height="14" viewBox="0 0 24 16" fill="none" stroke="#2f6684" stroke-width="2"><path d="M1 8s4-7 11-7 11 7 11 7-4 7-11 7S1 8 1 8z"/><circle cx="12" cy="8" r="3"/></svg>
      <span style="margin-left:10px">2</span><span class="link">Write Comments</span>
      <svg class="heart" width="20" height="18" viewBox="0 0 24 22" fill="none" stroke="#1f8fd3" stroke-width="2"><path d="M12 20S2 13.5 2 7a5 5 0 0 1 10-1 5 5 0 0 1 10 1c0 6.5-10 13-10 13z"/></svg>
    </div>
  </article>
  <article class="news-card" style="left:796px">
    <div class="news-photo" role="img" aria-label="Volunteer gardening outdoors" style="background:linear-gradient(160deg,#b7d08a,#6f9a4a 55%,#4a7034)"></div>
    <h3>10 Ways You Can Get Involved<br>In Your Community!</h3>
    <div class="news-meta">
      <svg width="20" height="14" viewBox="0 0 24 16" fill="none" stroke="#2f6684" stroke-width="2"><path d="M1 8s4-7 11-7 11 7 11 7-4 7-11 7S1 8 1 8z"/><circle cx="12" cy="8" r="3"/></svg>
      <span style="margin-left:10px">2</span><span class="link">Write Comments</span>
      <svg class="heart" width="20" height="18" viewBox="0 0 24 22" fill="none" stroke="#1f8fd3" stroke-width="2"><path d="M12 20S2 13.5 2 7a5 5 0 0 1 10-1 5 5 0 0 1 10 1c0 6.5-10 13-10 13z"/></svg>
    </div>
  </article>
</section>

<footer class="site-footer">
  <div class="footer-head" style="left:79px">Contact</div>
  <div class="footer-phone">123-456-7890</div>
  <div class="footer-mail">info@harborlightchurch.com</div>
  <div class="footer-head" style="left:437px">Stay Updated</div>
  <div class="newsletter"><span>Register for our Newsletter...</span>
    <svg width="22" height="16" viewBox="0 0 22 16" fill="none" stroke="#333" stroke-width="2"><path d="M2 2l6 6-6 6M11 2l6 6-6 6"/></svg>
  </div>
  <div class="footer-head" style="left:863px">Social Media</div>
  <div class="social"><span aria-label="Social profile one"></span><span aria-label="Social profile two"></span><span aria-label="Social profile three"></span></div>
  <div class="footer-rule"></div>
  <div class="copyright">Copyright © <strong><em>HARBOR LIGHT CHURCH</em></strong> - 2018 . All Right Reserved</div>
  <div class="legal">Terms &amp; Conditions &nbsp; | &nbsp; Privacy policy</div>
</footer>

</body>
</html>
```